Tarn - Stationary Design/Layout

We are a well established clothing design and manufacturing company (Tarn Sourcing) based in London UK, with our own factory in Bangladesh, supplying to many fashion retailers and brands. Our factory has very high environmental and ethical standards with people at its heart. Our quality of garments are second to none.
Our new logo has been proudly developed by the Pixel Guild community last month, we are now in the second phase and need the layout designed for our letterheads, double sided business cards, compliment slip and clothing ticket. Feel as creative as you like, but make sure it looks great!!
***The Logo - the logo design and colour is set and should NOT be changed and stay on a dark grey backround. The logo artwork to use is attached.
***Details to use for the business card:
Dorian Pelham
Direct Line: 020 7946 0158
dorian@tarnsourcing-example.com
Tarn Sourching Ltd.
57 - 59 Hollin Row
Camdon . Swindon
NW9 4QT
Switchboard: 020 7946 0274
Fax: 020 7946 0274
www.tarnsourcing-example.co.uk
***Details to use for the letterhead and compliment slip:
Tarn Sourching Ltd.
57 - 59 Hollin Row
Camdon . Swindon
NW9 4QT
Fax: 020 7946 0274
www.tarnsourcing-example.co.uk
***Details for Swing Ticket:
Size: 12cm height by 5.5cm width
One side need to have just the logo without the 'Sourcing', on the other it needs to stay blank

```html
<!DOCTYPE html>
<html lang="en">
<head>
<meta charset="utf-8">
<title>Tarn Sourcing – Compliment Slip</title>
<link rel="stylesheet" href="https://fonts.googleapis.com/css2?family=Crimson+Pro:wght@400&display=swap">
<style>
  :root {
    --slate: #3d3d3d;
    --aqua: #abe0e4;
    --font-text: "Crimson Pro", "Palatino Linotype", Palatino, serif;
  }
  html, body {
    margin: 0;
    padding: 0;
    width: 1200px;
    height: 566px;
    overflow: hidden;
    background: var(--slate);
  }
  .slip {
    position: relative;
    width: 1200px;
    height: 566px;
    background: var(--slate);
    font-family: var(--font-text);
    color: var(--aqua);
  }
  .brand-name {
    position: absolute;
    left: 111px;
    top: 222px;
    margin: 0;
    font-family: var(--font-text);
    font-weight: 400;
    font-size: 74px;
    line-height: 1;
    letter-spacing: 1px;
    color: var(--aqua);
    white-space: nowrap;
  }
  .contact {
    position: absolute;
    right: 33px;
    top: 19px;
    margin: 0;
    text-align: right;
    font-style: normal;
    font-size: 21.5px;
    line-height: 26.5px;
  }
  .contact p {
    margin: 0;
  }
  .contact .lines + .lines {
    margin-top: 27px;
  }
</style>
</head>
<body>
  <main class="slip">
    <h1 class="brand-name">Tarn Sourcing</h1>

    <address class="contact">
      <div class="lines postal">
        <p>Tarn Sourching Ltd.</p>
        <p>57 - 59 Hollin Row</p>
        <p>Camdon . Swindon</p>
        <p>NW9 4QT</p>
      </div>
      <div class="lines telecom">
        <p>Switchboard: 020 7946 0274</p>
        <p>Fax: 020 7946 0274</p>
        <p>www.tarnsourcing-example.co.uk</p>
      </div>
    </address>
  </main>
</body>
</html>
```